Dentistry

Dentist's personal business card. No logo needed. The card shoul deliver the massage of reliability, professionalism, experience.
Please ad the full brief of the project: down the line it says: the winning look should be precise and pristine NO pictures of Teeth, smiles, instruments etc.

The details to be desplaid are:
Dr. Rob Valdoni
Doctor of Dental Surgery
PHD
Web. Www.drvaldoni.com
Email. Rob@drvaldoni.com
Tel 07731482590
Surgery address. 27Bharwick road London SW4 7QN UK
82 Fenwyn Row London SW3 2HT. Uk

Reason: Decided to make the payment unrefundable in order to get more designers involved.

Requirements
Should not have
• Logo, teeth, smile any sort of instruments.

```html
<!DOCTYPE html>
<html lang="en">
<head>
<meta charset="utf-8">
<title>Dr. Rob Valdoni – Business Card</title>
<link rel="stylesheet" href="https://fonts.googleapis.com/css2?family=PT+Sans:wght@400;700&display=swap">
<style>
  :root {
    --page-bg: #ececec;
    --card-bg: #ffffff;
    --navy: #1b2379;
    --orange: #f07f1a;
    --white: #ffffff;
  }
  * { margin: 0; padding: 0; box-sizing: border-box; }
  html, body {
    width: 1200px;
    height: 760px;
    overflow: hidden;
    background: var(--page-bg);
    font-family: "PT Sans", Arial, sans-serif;
  }
  .business-card {
    position: absolute;
    left: 70px;
    top: 55px;
    width: 1060px;
    height: 650px;
    background: var(--card-bg);
    color: var(--navy);
    text-align: center;
  }
  .header-band {
    position: absolute;
    left: 0;
    top: 0;
    width: 100%;
    height: 282px;
    background: var(--navy);
    border-radius: 0 0 24px 24px;
    color: var(--white);
  }
  .doctor-name {
    position: absolute;
    top: 86px;
    width: 100%;
    font-size: 38px;
    font-weight: 700;
    line-height: 1;
  }
  .doctor-title {
    position: absolute;
    top: 138px;
    width: 100%;
    font-size: 38px;
    font-weight: 400;
    line-height: 1;
  }
  .doctor-degree {
    position: absolute;
    top: 188px;
    width: 100%;
    font-size: 38px;
    font-weight: 400;
    line-height: 1;
  }
  .website-pill {
    position: absolute;
    left: 197px;
    top: 251px;
    width: 606px;
    height: 76px;
    background: var(--orange);
    border-radius: 14px;
    color: var(--white);
    font-size: 48px;
    font-weight: 700;
    line-height: 76px;
  }
  .contact-line {
    position: absolute;
    width: 100%;
    display: flex;
    justify-content: center;
    align-items: center;
    gap: 22px;
    font-size: 34px;
    font-weight: 700;
    line-height: 1;
  }
  .contact-line svg { flex: none; }
  .contact-phone { top: 364px; }
  .contact-email { top: 424px; }
  .email-rule {
    position: absolute;
    left: 370px;
    top: 476px;
    width: 328px;
    height: 4px;
    background: var(--orange);
  }
  .surgery-address {
    position: absolute;
    top: 510px;
    width: 100%;
    font-size: 28px;
    font-weight: 400;
    line-height: 36px;
  }
</style>
</head>
<body>
  <div class="business-card">
    <div class="header-band">
      <div class="doctor-name">Dr. Rob Valdoni</div>
      <div class="doctor-title">Doctor of Dental Surgery</div>
      <div class="doctor-degree">PHD</div>
    </div>
    <div class="website-pill">www.drvaldoni.com</div>

    <div class="contact-line contact-phone">
      <svg width="28" height="28" viewBox="0 0 24 24" aria-hidden="true">
        <path fill="#1b2379" d="M6.6 10.8c1.4 2.8 3.8 5.1 6.6 6.6l2.2-2.2c.3-.3.7-.4 1-.2 1.1.4 2.3.6 3.6.6.6 0 1 .4 1 1V20c0 .6-.4 1-1 1C10.6 21 3 13.4 3 4c0-.6.4-1 1-1h3.5c.6 0 1 .4 1 1 0 1.3.2 2.5.6 3.6.1.3 0 .7-.2 1l-2.3 2.2z"/>
      </svg>
      <span>07731482590</span>
    </div>

    <div class="contact-line contact-email">
      <svg width="30" height="22" viewBox="0 0 30 22" aria-hidden="true">
        <rect x="1.5" y="1.5" width="27" height="19" fill="none" stroke="#1b2379" stroke-width="2.5"/>
        <path d="M1.5 1.5 L15 12 L28.5 1.5" fill="none" stroke="#1b2379" stroke-width="2.5"/>
      </svg>
      <span>rob@drvaldoni.com</span>
    </div>
    <div class="email-rule"></div>

    <div class="surgery-address">
      Surgery address: 27Bharwick road London SW4 7QN UK<br>
      82 Fenwyn Row London SW3 2HT. Uk
    </div>
  </div>
</body>
</html>
```